Contractor Plan "B"/Getting Screwed?/Something Useful

We are sending out a series of postcards to a group of local contractors.

The first in the series is: Plan B: Pink Bubble Wrap. Plan A is to buy insurance from my agency. This will be printed, front and back on card stock. We will then glue a piece of bubble wrap to the card and place it in an envelope for delivery.

The second card will be along the same lines but will ask if the client is getting screwed by his current Insurance Company. We will glue a screw in the middle of the card and place the card in an envelope for delivery. On the bottom of we might tell them to call us to get unscrewed.

The third card will follow those lines but say something like: We sent you bubble wrap for your Plan B and you didn't call. Then we sent you something funny but you didn't call. We decided to send you something useful so you might call now! With this card, we are going to send a carpenter pencil.

I am attaching a rough outline of my sketch design for the first card so you will have basic information we will need such as phone number and coverages we offer. If you feel like there is too much info for the size of the card, we can leave some off. I just want the phone to ring! Also, feel free to adjust the wording to make it work better...creative design is not my strong suit!!

I would like for all three cards to be designed. Each can have the same backside. Also, please keep in mind, this is not a postcard so you don't have to leave the blanks on the back for addressing. Each will be mailed in an envelope.

I have also uploaded my logo file as we have recently redone the logo.

Here is more guidance on the project: The cards are going to be 10 cm wide and 23 cm tall. I have added more wording in the brief. Also, I attached a word doc with a good idea of what to use for wording. Basically I want the following idea: Card 1: At top of card - Plan B: Pink Bubble Wrap Below the bubble wrap - Plan A: Call us so you don't have to use Pink Bubble Wrap Card 2: At top of card - Getting Screwed? Is your current agent taking you for granted? Below the area where we are going to glue a screw - Get unscrewed, Call us! Card 3: At top of card - We have the sharpest pencil in town! We will leave space for a carpenter pencil to be attached tot he card. On the other side of the open space - Call us today for the best rates on your insurance!

Please review the attached word doc for an idea of what to put on the back of the card. To be clear, we need three designs for the front of the card and can probably use just one design for the back of all three. If you think we need to have a different design for the back of each, I would like to see your ideas. Thank you for your hard work on these!

Reason: Hi, I am extending the time as I am expecting a few more submissions. Thank you!

Target Market(s)

We are targeting both contractors and truckers with this campaign.

Industry/Entity Type

Insurance

Requirements
Must have
• Clever wording. It needs to be a call to action and doesn't need to have too many specifics.

We also have to have space in the middle to glue the bubble wrap on the first card, the screw in the second and attach the pencil in the third.

```html
<!DOCTYPE html>
<html lang="en">
<head>
<meta charset="utf-8">
<title>Getting Screwed? – Contractor Card</title>
<link rel="stylesheet" href="https://fonts.googleapis.com/css2?family=Anton&family=Oswald:wght@400;500&family=Arimo:wght@400&display=swap">
<style>
  :root {
    --ink: #0d0d0d;
    --accent: #c1272d;
    --paper: #ffffff;
    --steel-light: #f1f2f3;
    --steel-mid: #c9cbce;
    --muted: #444444;
  }
  * { margin: 0; padding: 0; box-sizing: border-box; }
  html, body {
    width: 1200px;
    height: 2756px;
    overflow: hidden;
    background: var(--paper);
  }
  .card {
    position: relative;
    width: 1200px;
    height: 2756px;
    background: var(--paper);
  }
  .headline {
    position: absolute;
    left: 0;
    width: 100%;
    text-align: center;
    font-family: "Anton", "Impact", sans-serif;
    font-weight: 400;
    line-height: 1;
    transform-origin: top center;
    white-space: nowrap;
  }
  .headline--getting {
    top: 50px;
    font-size: 330px;
    color: var(--ink);
    transform: scaleY(1.58);
    letter-spacing: -4px;
  }
  .headline--screwed {
    top: 712px;
    font-size: 197px;
    color: var(--accent);
    transform: scaleY(1.58);
    letter-spacing: -2px;
  }
  .subhead {
    position: absolute;
    top: 1020px;
    left: 205px;
    width: 780px;
    text-align: center;
    font-family: "Arimo", "Arial", sans-serif;
    font-size: 52px;
    line-height: 1.25;
    color: var(--ink);
  }
  .attach-area {
    position: absolute;
    top: 1180px;
    left: 240px;
    width: 720px;
    height: 720px;
  }
  .attach-area__placeholder {
    width: 100%;
    height: 100%;
    background: radial-gradient(ellipse at 50% 50%, var(--steel-mid) 0%, var(--steel-light) 45%, var(--paper) 70%);
  }
  .cta {
    position: absolute;
    top: 2068px;
    left: 0;
    width: 100%;
    text-align: center;
    font-family: "Oswald", "Arial Narrow", sans-serif;
    font-weight: 400;
    font-size: 122px;
    line-height: 1.1;
    color: var(--ink);
    letter-spacing: -1px;
    white-space: nowrap;
  }
  .phone {
    position: absolute;
    top: 2222px;
    left: 0;
    width: 100%;
    text-align: center;
    font-family: "Oswald", "Arial Narrow", sans-serif;
    font-weight: 500;
    font-size: 92px;
    line-height: 1.1;
    color: var(--accent);
  }
  .brand {
    position: absolute;
    top: 2450px;
    left: 0;
    width: 100%;
    text-align: center;
    font-family: "Oswald", "Arial Narrow", sans-serif;
    font-weight: 500;
    font-size: 62px;
    line-height: 1;
    color: var(--accent);
    letter-spacing: 2px;
  }
  .address {
    position: absolute;
    top: 2610px;
    left: 0;
    width: 100%;
    text-align: center;
    font-family: "Arimo", "Arial", sans-serif;
    font-size: 35px;
    color: var(--muted);
  }
</style>
</head>
<body>
  <main class="card">
    <h1 class="headline headline--getting">Getting</h1>
    <h2 class="headline headline--screwed">Screwed?</h2>
    <p class="subhead">Is your current agent taking you for granted?</p>

    <div class="attach-area">
      <div class="attach-area__placeholder" role="img" aria-label="Photo of a silver wood screw lying diagonally, marking where the real screw is glued"></div>
    </div>

    <p class="cta">Get unscrewed, Call us!</p>
    <p class="phone">281-555-0147</p>

    <p class="brand">CEDAR LINE INSURANCE</p>
    <p class="address">4810 Birchwood Ln, Maple Falls, Texas 77012</p>
  </main>
</body>
</html>
```